Plakat-Design für Musikwettbewerb-Veranstalter
Zielgruppe
Wir veranstalten Musikwettbewerbe an Schulen. Zielgruppe sind Schüler und ihre Eltern, männlich/weiblich 40/60, u25/ü25 ca. 50/50
Aufgabenstellung
Wir sind gespannt, gerne frei denken, Logo anbei, weitere Infos auf der Homepage www.klangfuchs-wettbewerb.de, Inhalte lt. altem Plakat (ebenfalls anbei)

```html
<!DOCTYPE html>
<html lang="de">
<head>
<meta charset="utf-8">
<title>Klangfuchs – Vorentscheid Nordstadt</title>
<link href="https://fonts.googleapis.com/css2?family=Roboto+Slab:wght@700;800&display=swap" rel="stylesheet">
<style>
  :root {
    --page: #d9d9d9;
    --paper: #fffdf6;
    --red: #d71f26;
    --green: #35e63a;
    --slate: #3f5566;
    --black: #111111;
    --yellow: #fbbf3a;
    --ink: #111111;
    --alert: #e3141b;
    --white: #ffffff;
    --warm-light: #fde9b8;
    --warm-mid: #f9c772;
  }
  * { box-sizing: border-box; margin: 0; padding: 0; }
  html, body { width: 1200px; height: 675px; overflow: hidden; }
  body {
    background: var(--page);
    font-family: "Roboto Slab", Georgia, serif;
    font-weight: 700;
    color: var(--ink);
    position: relative;
  }
  .poster {
    position: absolute;
    left: 370px; top: 8px;
    width: 460px; height: 650px;
    background: var(--paper);
    overflow: hidden;
  }
  .poster__backdrop {
    position: absolute; inset: 130px 0 40px 0;
    background: radial-gradient(ellipse at 70% 55%, #f6a24a 0%, #f9c772 35%, #fde8b4 65%, rgba(255,253,246,0) 90%);
  }
  .header-art {
    position: absolute; left: 30px; top: 6px; width: 280px; height: 136px;
    background: radial-gradient(ellipse at 50% 55%, var(--warm-mid) 0%, var(--warm-light) 55%, rgba(255,253,246,0) 100%);
  }
  .brand-name {
    position: absolute; left: 30px; top: 52px; width: 280px;
    text-align: center;
    font-size: 40px; font-weight: 800; color: var(--ink);
    white-space: nowrap;
  }
  .band { position: absolute; }
  .band svg { position: absolute; inset: 0; width: 100%; height: 100%; }
  .band__text { position: relative; color: var(--white); line-height: 1; white-space: nowrap; }
  .band--title { left: 22px; top: 150px; width: 388px; height: 66px; }
  .band--title .band__text { font-size: 40px; padding: 16px 0 0 14px; transform: rotate(-2deg); }
  .band--city { left: 197px; top: 200px; width: 230px; height: 60px; }
  .band--city .band__text { font-size: 46px; padding: 4px 0 0 12px; }
  .band--date { left: 75px; top: 262px; width: 385px; height: 112px; }
  .band--date .band__text { font-size: 46px; text-align: center; padding: 8px 30px 0 0; transform: rotate(-2deg); line-height: 1.05; }
  .band--venue { left: 0; top: 384px; width: 336px; height: 94px; }
  .band--venue .band__text { font-size: 19px; text-align: center; padding: 10px 10px 0 0; line-height: 1.15; transform: rotate(-2deg); }
  .info {
    position: absolute; left: 0; top: 477px; width: 460px; height: 137px;
    background: var(--yellow);
  }
  .info__address {
    position: absolute; left: 4px; top: 31px; width: 218px;
    text-align: center; font-size: 15px; line-height: 16px; white-space: nowrap;
  }
  .info__times {
    position: absolute; left: 226px; top: 20px;
    font-size: 24px; line-height: 26px; white-space: nowrap;
  }
  .info__call {
    position: absolute; left: 0; top: 101px; width: 100%;
    text-align: center; font-size: 12.5px; color: var(--alert); white-space: nowrap;
  }
  .info__links {
    position: absolute; left: 0; top: 117px; width: 100%;
    text-align: center; font-size: 12.5px; white-space: nowrap;
  }
  .sponsors {
    position: absolute; left: 0; top: 614px; width: 460px; height: 36px;
    background: var(--white); border-top: 2px solid var(--black);
    display: flex; justify-content: center; align-items: center; gap: 14px;
    font-size: 11px; color: var(--slate);
  }
</style>
</head>
<body>
  <main class="poster">
    <div class="poster__backdrop" role="img" aria-label="Warmer Hintergrund aus verschwommenen Musiknoten in Gelb und Orange"></div>

    <div class="header-art" role="img" aria-label="Illustration mit Musikinstrumenten hinter dem Veranstalternamen"></div>
    <div class="brand-name">Klangfuchs</div>

    <div class="band band--title">
      <svg viewBox="0 0 388 66" preserveAspectRatio="none"><polygon points="12,12 372,0 388,50 0,66" fill="var(--red)"/></svg>
      <div class="band__text">VORENTSCHEID</div>
    </div>

    <div class="band band--city">
      <svg viewBox="0 0 230 60" preserveAspectRatio="none"><polygon points="6,4 226,0 230,56 0,60" fill="var(--green)"/></svg>
      <div class="band__text">Nordstadt</div>
    </div>

    <div class="band band--date">
      <svg viewBox="0 0 385 112" preserveAspectRatio="none"><polygon points="30,6 355,0 385,72 350,102 0,112" fill="var(--slate)"/></svg>
      <div class="band__text">11.07.2016<br>Ab 19:00 Uhr</div>
    </div>

    <div class="band band--venue">
      <svg viewBox="0 0 336 94" preserveAspectRatio="none"><polygon points="0,4 310,0 336,76 0,94" fill="var(--black)"/></svg>
      <div class="band__text">Lindenhof-Schule<br>Berufliche Schule Nordstadt<br>Gemeinschaftsschule Nordstadt</div>
    </div>

    <section class="info">
      <div class="info__address">Mensa der<br>Lindenhof-Schule<br>Lindenhofweg 5<br>25000 Nordstadt</div>
      <div class="info__times">Einlass: 18:30 Uhr<br>Beginn: 19:00 Uhr<br>Vvk: 3 € | Ak: 4 €</div>
      <p class="info__call">Bewerbung für Künstler unter www.klangfuchs-wettbewerb.de/bewerbung</p>
      <p class="info__links">www.klangfuchs-wettbewerb.de | www.klangfuchs-community.de</p>
    </section>

    <footer class="sponsors">
      <span>Kreiskasse</span>
      <span>Klangwerk</span>
      <span>Tonrecht</span>
      <span>Tonhaus</span>
      <span>Land Nord Bildung</span>
    </footer>
  </main>
</body>
</html>
```